Design für satanierte Visitenkarten (transparent)
Zielgruppe
Wir sind ein Online Bildportal, bei dem man wie z. B. Pixanda, Lumoraframes und Brightcrate Bilder hochladen und verkaufen kann.
Unterschied zu den o. g. Portalen ist, dass wir uns auf den Exklusivmarkt fokusieren und der Künstler mind. 50% des Umsatzes erhält. Wichtig ist uns, dass sowohl der Kunde als auch der Fotograf/Grafiker Gewinner bei dem Handel sind (Win-Win-Situation)
Unsere Zeilgruppen:
Anbieter: Fotografen, Hobbyfotografen und Grafiker
Kunden: Marketingfirmen jeglicher Art
Aufgabenstellung
Wir benötigen ein Visitenkarten-Design, welches auf satinierte PVC-Visitenkarten (transparent) mit abgerundeten Ecken aufgedruckt wird. In der Design-Datei müssen sämtliche Variablen wie Name, Tel. etc. durch kurzes anklicken und reinschreiben austauschbar sein.
Unser Logo muss miteingebunden werden und sollte schön groß zu erkennen sein. Sollten dennoch Ideen aufkommen, bei denen dies etwas anders aussieht, lassen wir uns gerne überraschen.
Da das Ganze auf transparente Visitenkarten kommt, möchten wir, dass der Hintergrund beim Logo frei bleibt. Ein farbiger Hintergrund bei den Infos ist ok. Ein Hintergrund mit dem Farbcode #ededed wäre sehr passend, da sich auf der Webseite ebenfalls ein Balken mit abgerundeten Ecken befindet, welcher diesen Farbcode enthält.
Folgende Infos sollten enthalten sein:
- Name
- Position (Geschäftsführer etc.)
- Adresse
- Tel.
- Fax.
- Email
- Webadresse
Die Visitenkarten werden folgende Maße aufweisen:
Entwurfformat: 9 x 6 cm
Entformat: 8,5 x 5,5 cm
Folgende Punkte müssen laut Pruckerei beachtet werden:
Dateiformat: Das beste Druckergebnis erhalten Sie mit Vorlagen im Vektorformat (.ai und .eps ). Bitte senden Sie uns die Datei mit offenen Ebenen, die Texte in Pfade gewandelt oder gerastert (ansonsten ggf. den Font separat. Dies gilt auch für PDFs, da der Druck mit Illustrator vorbereitet wird!). Die Erstellung einer Stanzform oder eines Prägeklischees ist nur mit Vektordaten möglich.
Farbraum: Senden Sie uns die Daten unbedingt in CMYK (Coated FOGRA27). Die Umwandlung von RGB- in CMYK-Daten kann zu Farbabweichungen führen, daher nehmen Sie die Umwandlung bitte ggf. vor der Einsendung Ihrer Datei selbst vor. Wenn Ihr Design weiße Elemente enthalten soll, können Sie diese in 100% Cyan anlegen. Bitte fügen Sie dann eine Notiz wie "Cyan = Weiß" bei.
Beschnittzugabe: Zur Gestaltung von..

```html
<!DOCTYPE html>
<html lang="de">
<head>
<meta charset="utf-8">
<title>lumivista – Visitenkarte</title>
<link rel="stylesheet" href="https://fonts.googleapis.com/css2?family=Crimson+Text:wght@400;700&display=swap">
<style>
  :root {
    --backdrop: #8a8a8a;
    --card-clear: rgba(255, 255, 255, 0.10);
    --card-edge: rgba(255, 255, 255, 0.65);
    --info-panel: #efedee;
    --ink: #2a211c;
    --berry: #a53d69;
    --violet: #7f4a98;
  }
  * { margin: 0; padding: 0; box-sizing: border-box; }
  html, body {
    width: 1200px;
    height: 1200px;
    overflow: hidden;
    background: var(--backdrop);
    font-family: "Crimson Text", serif;
  }
  .business-card {
    position: absolute;
    left: 294px;
    top: 201px;
    width: 619px;
    height: 401px;
    border-radius: 25px;
    background: var(--card-clear);
    border: 1px solid var(--card-edge);
    overflow: hidden;
  }
  .brand {
    position: absolute;
    left: 70px;
    top: 60px;
    display: flex;
    align-items: center;
    gap: 22px;
  }
  .brand-dot {
    width: 58px;
    height: 58px;
    border-radius: 50%;
    background: var(--berry);
  }
  .brand-name {
    font-size: 100px;
    line-height: 1;
    font-weight: 400;
    color: var(--berry);
  }
  .divider {
    position: absolute;
    left: 0;
    top: 205px;
    width: 100%;
    height: 11px;
    display: flex;
  }
  .divider-dark { width: 360px; background: var(--ink); }
  .divider-berry { flex: 1; background: var(--berry); }
  .info-panel {
    position: absolute;
    left: 0;
    top: 216px;
    width: 100%;
    height: 185px;
    background: var(--info-panel);
  }
  .person {
    position: absolute;
    left: 30px;
    top: 16px;
    color: var(--violet);
  }
  .person-first { font-size: 31px; line-height: 32px; }
  .person-last { font-size: 31px; line-height: 32px; font-weight: 700; letter-spacing: 0.5px; }
  .person-role { font-size: 22px; line-height: 30px; margin-top: 4px; }
  .contact {
    position: absolute;
    left: 370px;
    top: 14px;
    color: var(--ink);
    font-size: 21px;
    line-height: 24px;
    list-style: none;
  }
  .contact li { white-space: nowrap; }
  .contact .gap { margin-top: 3px; }
  .contact .web { font-weight: 700; }
  .confetti {
    position: absolute;
    left: 82px;
    top: 124px;
    width: 278px;
    height: 48px;
    background: linear-gradient(100deg, rgba(40,160,220,0.35), rgba(210,215,30,0.35) 45%, rgba(235,120,50,0.35) 75%, rgba(225,40,60,0.35));
    border-radius: 6px;
  }
</style>
</head>
<body>
  <article class="business-card">
    <header class="brand">
      <span class="brand-dot"></span>
      <span class="brand-name">lumivista</span>
    </header>

    <div class="divider">
      <span class="divider-dark"></span>
      <span class="divider-berry"></span>
    </div>

    <section class="info-panel">
      <div class="person">
        <p class="person-first">Lukas</p>
        <p class="person-last">BRENNER</p>
        <p class="person-role">Geschäftsführer</p>
      </div>

      <div class="confetti" role="img" aria-label="Verstreute bunte Dreiecke in Blau, Gelbgrün, Orange und Rot"></div>

      <ul class="contact">
        <li>Talmühlstraße 7</li>
        <li>81249 München</li>
        <li class="gap">Tel. +49 (0)89 41527380</li>
        <li>Fax +49 (0)89 41527381</li>
        <li class="gap">kontakt@lumivista.com</li>
        <li class="web">www. lumivista.com</li>
      </ul>
    </section>
  </article>
</body>
</html>
```